KORVA - 7 Rack Card (Nutritional Supplement Rack Card)

I have a nutritional supplement line that focuses on reducing inflammation. I need a line of rack cards to promote each of my supplements / condition kits. The company is www.Korva-Supplements.example and www.Korva-Meals.example. This first design should focus on my KORVA - 7 supplements. All of these supplements are designed to reduce inflammation. A lot of information about each can be found on my website www.Korva-Supplements.example to be used in the rack card. Please use as many bullet points as possible rather than long paragraphs of text.

Target Market(s)

People dealing with inflammation and disease. People wishing to take nutritional supplements and people interested in natural health.

Industry/Entity Type

Supplement

Font styles to use
Other font styles liked:
• I usually like the look of Avenir font

Colors
0692cd
0255a3
ec1f27
f37122

Requirements
Must have
• Must have my logo
• Must have a clean modern design that includes information about each supplement in my KORVA - 7 pack
• Must allow people to clearly understand the importance of each supplement
• Must be brief and to the point
Nice to have
• Anything that demonstrates reducing inflammation naturally
• Healthy people enjoying life
Should not have
• Busy design that is overwhelmed with information

```html
<!DOCTYPE html>
<html lang="en">
<head>
<meta charset="utf-8">
<title>KORVA - 7 Rack Card</title>
<link rel="stylesheet" href="https://fonts.googleapis.com/css2?family=Nunito+Sans:wght@400;600;700;800;900&display=swap">
<style>
:root{
  --sky:#0692cd;
  --navy:#0255a3;
  --red:#ec1f27;
  --orange:#f37122;
  --ink:#1d1d1b;
  --paper:#ffffff;
  --mist:#e6f2fa;
  --stage:#ececec;
  --rule:#b9c3cc;
}
*{box-sizing:border-box;margin:0;padding:0}
html,body{width:1200px;height:1000px;overflow:hidden}
body{background:var(--stage);font-family:"Nunito Sans",Arial,sans-serif;color:var(--ink);position:relative}
.card{position:absolute;top:44px;width:407px;height:914px;background:var(--paper);overflow:hidden;box-shadow:0 4px 14px rgba(0,0,0,.25)}
.card--front{left:148px}
.card--back{left:643px}
.abs{position:absolute}
.waves{position:absolute;left:0;width:100%}
.brand{position:absolute;display:flex;align-items:center}
.brand__dot{border-radius:50%;background:var(--sky);flex:none}
.brand__name{font-weight:900;color:var(--ink);line-height:.95;letter-spacing:.5px}
.brand__name span{display:block}
.tagline{top:138px;left:0;width:100%;text-align:center;color:var(--navy);font-weight:700;font-size:16px;letter-spacing:.2px}
.photo{background:linear-gradient(180deg,#dfeef8 0%,#f4f1e6 45%,#c9c48a 70%,#7d9a3c 100%)}
.bottles{background:linear-gradient(180deg,#3a1f14 0%,#6b2f17 50%,#2c160d 100%);border-radius:6px;opacity:.92}
.intro{top:729px;left:26px;width:356px;font-size:11.4px;line-height:1.22;text-align:justify;letter-spacing:-.1px}
.red{color:var(--red);font-weight:700}
.kit{top:780px;left:38px;width:340px;display:grid;grid-template-columns:1fr 1fr;row-gap:4px;color:var(--navy);font-size:18px;font-weight:600}
.kit li{list-style:none;display:flex;align-items:center;gap:4px}
.tick{display:inline-block;width:11px;height:11px;border:1.5px solid var(--red);position:relative;flex:none}
.tick::after{content:"";position:absolute;left:2px;top:-1px;width:4px;height:7px;border:solid var(--red);border-width:0 2px 2px 0;transform:rotate(40deg)}
.kit .tick{width:13px;height:13px}
.footer{position:absolute;left:0;bottom:0;width:100%;height:80px}
.footer__text{position:absolute;left:0;width:100%;text-align:center;color:#fff;font-weight:700}
.footer__url{top:27px;font-size:17px}
.footer__mail{top:50px;font-size:14px;font-weight:600}
.ico{display:inline-block;vertical-align:-2px;margin-right:5px}
.headline{top:86px;left:0;width:100%;text-align:center;color:var(--red);font-weight:800;font-size:12px;line-height:1.2}
.item{position:absolute;left:35px;width:350px}
.item__bottle{position:absolute;left:0;width:80px;border-radius:6px}
.item__label{position:absolute;left:95px;top:0;background:var(--red);color:#fff;font-weight:700;font-size:13px;padding:1px 7px;border-radius:2px}
.item__body{position:absolute;left:95px;top:24px;width:247px;font-size:7.9px;line-height:1.33;text-align:justify;letter-spacing:-.05px}
.bullets{display:flex;gap:8px;margin-top:8px;text-align:left}
.bullets ul{list-style:none;flex:1}
.bullets li{display:flex;gap:4px;font-size:9px;line-height:1.3}
.bullets .tick{width:7px;height:7px;border-width:1px;margin-top:3px;border-color:var(--navy)}
.bullets .tick::after{left:1px;top:-1px;width:2px;height:4px;border-color:var(--navy);border-width:0 1px 1px 0}
.divider{position:absolute;left:130px;width:245px;height:1px;background:var(--rule)}
.closing{top:790px;left:30px;width:347px;font-size:12px;line-height:1.2;text-align:justify}
</style>
</head>
<body>

<section class="card card--front">
  <svg class="waves" style="top:0" width="407" height="120" viewBox="0 0 407 120">
    <path d="M0 40 Q200 10 407 30 L407 0 L0 0Z" fill="var(--mist)"/>
    <path d="M0 45 Q210 15 407 38" stroke="#bcdcef" stroke-width="2" fill="none"/>
  </svg>
  <div class="brand" style="top:20px;left:45px">
    <div class="brand__dot" style="width:112px;height:112px"></div>
    <div class="brand__name" style="margin-left:26px;font-size:46px">KORVA<span style="font-size:29px">Supplements</span></div>
  </div>
  <div class="abs tagline">MY ANTI-INFLAMMATORY NUTRITION</div>

  <div class="abs photo" style="top:162px;left:0;width:407px;height:440px" role="img" aria-label="Photo of a smiling family in a sunny meadow, a child riding on his father's shoulders"></div>
  <svg class="abs" style="top:455px;left:0" width="407" height="110" viewBox="0 0 407 110">
    <path d="M160 110 Q300 40 407 20 L407 48 Q300 70 220 110Z" fill="var(--orange)"/>
    <path d="M200 110 Q310 62 407 48 L407 72 Q320 85 260 110Z" fill="var(--sky)"/>
  </svg>
  <div class="abs bottles" style="top:545px;left:38px;width:333px;height:160px" role="img" aria-label="Product photo of four KORVA supplement bottles: Magnesium, Multi, Omega-3 and Vitamin D3"></div>

  <p class="abs intro">The <span class="red">KORVA - 7</span> are the most important supplements to help aid in reducing overall inflammation. These supplements should be the staple of all nutritional supplement programs. The KORVA - 7 includes:</p>
  <ul class="abs kit">
    <li><span class="tick"></span>Multivitamin</li>
    <li><span class="tick"></span>Magnesium</li>
    <li><span class="tick"></span>Vitamin D3</li>
    <li><span class="tick"></span>Fish Oil</li>
  </ul>

  <div class="footer">
    <svg width="407" height="80" viewBox="0 0 407 80" style="position:absolute;top:0;left:0">
      <path d="M0 18 Q200 -4 407 12 L407 80 L0 80Z" fill="var(--orange)"/>
      <path d="M0 14 Q200 -8 407 8" stroke="var(--navy)" stroke-width="3" fill="none"/>
    </svg>
    <div class="footer__text footer__url"><svg class="ico" width="14" height="14" viewBox="0 0 14 14"><circle cx="7" cy="7" r="6" fill="none" stroke="#fff" stroke-width="1.3"/><ellipse cx="7" cy="7" rx="2.6" ry="6" fill="none" stroke="#fff" stroke-width="1.1"/><path d="M1 7H13" stroke="#fff" stroke-width="1.1"/></svg>www.Korva-Supplements.example</div>
    <div class="footer__text footer__mail"><svg class="ico" width="15" height="11" viewBox="0 0 15 11"><rect x=".7" y=".7" width="13.6" height="9.6" fill="none" stroke="#fff" stroke-width="1.3"/><path d="M1 1L7.5 6.5L14 1" fill="none" stroke="#fff" stroke-width="1.2"/></svg>info@korva-meals.example</div>
  </div>
</section>

<section class="card card--back">
  <svg class="waves" style="top:0" width="407" height="90" viewBox="0 0 407 90">
    <path d="M0 30 Q200 0 407 22 L407 0 L0 0Z" fill="var(--mist)"/>
    <path d="M0 36 Q210 6 407 30" stroke="#bcdcef" stroke-width="2" fill="none"/>
  </svg>
  <div class="brand" style="top:18px;left:115px">
    <div class="brand__dot" style="width:62px;height:62px"></div>
    <div class="brand__name" style="margin-left:12px;font-size:28px">KORVA<span style="font-size:17px">Supplements</span></div>
  </div>
  <div class="abs headline">SUPPLEMENTS TO HELP REDUCE INFLAMMATION AND<br>REVERSE CHRONIC DISEASE</div>

  <div class="item" style="top:122px">
    <div class="item__bottle bottles" style="top:12px;height:145px" role="img" aria-label="Product photo of the KORVA Magnesium bottle"></div>
    <div class="item__label">Magnesium</div>
    <div class="item__body">
      <p>Magnesium provides a host of benefits for the body and can help alleviate symptoms of various diseases and even lessen the risk of developing them. When the body is deficient in magnesium, a plethora of issues can surface, including:</p>
      <div class="bullets">
        <ul>
          <li><span class="tick"></span>Heart disease</li>
          <li><span class="tick"></span>High blood pressure</li>
          <li><span class="tick"></span>Kidney and liver damage</li>
          <li><span class="tick"></span>Osteoporosis</li>
          <li><span class="tick"></span>Alzheimer's disease</li>
        </ul>
        <ul>
          <li><span class="tick"></span>Worsened menstrual symptoms</li>
          <li><span class="tick"></span>Behavioral disorders</li>
          <li><span class="tick"></span>Insomnia</li>
          <li><span class="tick"></span>Tooth decay</li>
          <li><span class="tick"></span>Muscle weakness<br>Migraines</li>
        </ul>
      </div>
    </div>
  </div>
  <div class="divider" style="top:283px"></div>

  <div class="item" style="top:292px">
    <div class="item__bottle bottles" style="top:0;height:145px" role="img" aria-label="Product photo of the KORVA Multi Iron Free bottle"></div>
    <div class="item__label">Multivitamin</div>
    <div class="item__body">
      <p>According to world famous biochemist and toxicologist Dr. Alan Mercer, PhD, "No matter how well you eat, take a multivitamin daily. It may just save your life."</p>
      <p>According to Dr. Mercer, vitamin and mineral deficiencies are the most serious cancer risks that many people face today. His research on nutritional deficiencies dates back decades, and his discoveries are nothing short of astounding.</p>
      <p>Americans are certainly not short of food, but that doesn't necessarily mean we are properly nourished.</p>
      <p>Research has shown that adding a multivitamin supplement each day can not only decrease the risk of certain cancers, but also heart disease, among others.</p>
    </div>
  </div>
  <div class="divider" style="top:450px"></div>

  <div class="item" style="top:459px">
    <div class="item__bottle bottles" style="top:0;height:145px" role="img" aria-label="Product photo of the KORVA Vitamin D3 5,000 IU bottle"></div>
    <div class="item__label">Vitamin D3</div>
    <div class="item__body">
      <p>Did you know that about 200 million Americans are deficient in this critical vitamin? Perhaps it's because it's been ingrained in our brains that we should be avoiding sunlight in order to prevent the onset of skin cancer or premature aging. Vitamin D deficiency is linked to:</p>
      <div class="bullets" style="margin-bottom:10px">
        <ul>
          <li><span class="tick"></span>Fatigue</li>
          <li><span class="tick"></span>Aches</li>
        </ul>
        <ul>
          <li><span class="tick"></span>Pains</li>
          <li><span class="tick"></span>And unfortunately other very serious diseases</li>
        </ul>
      </div>
      <p>the body needs between 2000 to 3000 IU of vitamin D each day from either dietary sources, sun exposure, and supplements.</p>
    </div>
  </div>
  <div class="divider" style="top:619px"></div>

  <div class="item" style="top:637px">
    <div class="item__bottle bottles" style="top:-12px;height:145px" role="img" aria-label="Product photo of the KORVA Omega-3 bottle"></div>
    <div class="item__label">Omega-3 (Fish Oil)</div>
    <div class="item__body">
      <p>Taking a fish oil supplement can top you up if the foods you're eating aren't giving you as much omega-3's as you require to be healthy. Studies have also concluded that fish oil can help alleviate other medical conditions such as:</p>
      <div class="bullets">
        <ul>
          <li><span class="tick"></span>Hypertension</li>
          <li><span class="tick"></span>High cholesterol</li>
          <li><span class="tick"></span>Stroke</li>
          <li><span class="tick"></span>Diabetes</li>
          <li><span class="tick"></span>Osteoporosis</li>
        </ul>
        <ul>
          <li><span class="tick"></span>Asthma</li>
          <li><span class="tick"></span>Depression</li>
          <li><span class="tick"></span>Weight loss</li>
          <li><span class="tick"></span>Bipolar disorder</li>
          <li><span class="tick"></span>Schizophrenia</li>
        </ul>
      </div>
    </div>
  </div>

  <p class="abs closing">The most effective way to reduce inflammation is by removing inflammatory foods from your diet. For a complete customized 16-week anti-inflammatory meal plan see:</p>

  <div class="footer">
    <svg width="407" height="80" viewBox="0 0 407 80" style="position:absolute;top:0;left:0">
      <path d="M0 18 Q200 -4 407 12 L407 80 L0 80Z" fill="var(--navy)"/>
      <path d="M0 14 Q200 -8 407 8" stroke="var(--orange)" stroke-width="3" fill="none"/>
    </svg>
    <div class="footer__text footer__url"><svg class="ico" width="14" height="14" viewBox="0 0 14 14"><circle cx="7" cy="7" r="6" fill="none" stroke="#fff" stroke-width="1.3"/><ellipse cx="7" cy="7" rx="2.6" ry="6" fill="none" stroke="#fff" stroke-width="1.1"/><path d="M1 7H13" stroke="#fff" stroke-width="1.1"/></svg>www.Korva-Meals.example</div>
    <div class="footer__text footer__mail"><svg class="ico" width="15" height="11" viewBox="0 0 15 11"><rect x=".7" y=".7" width="13.6" height="9.6" fill="none" stroke="#fff" stroke-width="1.3"/><path d="M1 1L7.5 6.5L14 1" fill="none" stroke="#fff" stroke-width="1.2"/></svg>info@korva-meals.example</div>
  </div>
</section>

</body>
</html>
```